Our architectural studio needs a new business card

We need a business card design for our studio based in Waterloo in Belgium. We are active in architecture, design and installation.
Our works are contemporary and minimalist. our clients are refined and cultured.
Our business card must be minimalist and refined.

Project Deadline Extended
Reason: Some designers have accepted my invitation but they don't have all replied. I want to give them a chance to make one proposal. Paul

Target Market(s)

architecture

Industry/Entity Type

Business

Contact Information for Business Card

studio: paul dornevaux studio
paul dornevaux, architecte
M. +32 471 586 927
F. +322 619 4850
www.pauldornevaux-example.com
paul@pauldornevaux-example.com
14 rue des Marronniers
1420 Waterloo
Belgium

Font styles to use
Sans Serif

Requirements
Must have
• simple, minimalist, clear, elegant and chic! Black and white
Nice to have
• embossed logo, other format like a square for example
Should not have
• color, fantasy, curves, ...

```html
<!DOCTYPE html>
<html lang="en">
<head>
<meta charset="utf-8">
<title>Paul Dornevaux Studio – Business Card</title>
<link rel="stylesheet" href="https://fonts.googleapis.com/css2?family=Exo+2:ital,wght@0,400;0,600;0,700;1,400&display=swap">
<style>
  :root {
    --page: #e6e4e1;
    --card: #ffffff;
    --card-shade: #eeeeee;
    --ink: #111111;
    --band: #0d0d0d;
    --stripe: #b9b9bb;
    --stripe-light: #d6d6d8;
    --text: #2a2a2a;
    --on-dark: #ffffff;
  }
  * { margin: 0; padding: 0; box-sizing: border-box; }
  html, body {
    width: 1200px; height: 901px; overflow: hidden;
    background: var(--page);
    font-family: "Exo 2", sans-serif;
  }
  .card {
    position: absolute; left: 110px; top: 170px;
    width: 980px; height: 560px;
    border-radius: 56px; overflow: hidden;
    background: radial-gradient(ellipse at 70% 60%, var(--card) 40%, var(--card-shade) 100%);
    box-shadow: 0 18px 40px rgba(0,0,0,.18);
  }
  .card-art { position: absolute; inset: 0; }
  .holder { position: absolute; left: 330px; top: 22px; color: var(--on-dark); }
  .holder-name { font-size: 40px; font-style: italic; font-weight: 400; letter-spacing: 1px; }
  .holder-role { font-size: 26px; font-style: italic; margin: 2px 0 0 70px; }
  .contacts { position: absolute; left: 70px; top: 300px; list-style: none; color: var(--text); }
  .contacts li { display: flex; align-items: center; gap: 14px; font-size: 24px; height: 40px; }
  .contacts svg { width: 22px; height: 22px; fill: var(--ink); flex: none; }
  .studio { position: absolute; left: 560px; top: 330px; display: flex; align-items: center; gap: 14px; }
  .studio-mark { width: 22px; height: 22px; background: var(--ink); }
  .studio-name { font-size: 22px; font-weight: 700; letter-spacing: 4px; text-transform: uppercase; color: var(--ink); }
  .address { position: absolute; right: 90px; top: 404px; text-align: right; font-size: 26px; line-height: 38px; font-style: normal; color: var(--text); }
</style>
</head>
<body>
<article class="card">
  <svg class="card-art" viewBox="0 0 980 560" aria-hidden="true">
    <polygon fill="var(--stripe-light)" points="0,176 980,136 980,162 0,216"/>
    <polygon fill="var(--stripe)" points="0,224 980,170 980,178 0,234"/>
    <polygon fill="var(--band)" points="0,0 980,0 980,126 0,166"/>
  </svg>

  <div class="holder">
    <p class="holder-name">Paul Dornevaux</p>
    <p class="holder-role">architecte</p>
  </div>

  <ul class="contacts">
    <li><svg viewBox="0 0 24 24"><path d="M7 1h10a2 2 0 0 1 2 2v18a2 2 0 0 1-2 2H7a2 2 0 0 1-2-2V3a2 2 0 0 1 2-2zm0 3v14h10V4zm5 15.5a1.2 1.2 0 1 0 0 2.4 1.2 1.2 0 0 0 0-2.4z"/></svg>M. +32 471 586 927</li>
    <li><svg viewBox="0 0 24 24"><path d="M6 2h9l3 3v6h2a2 2 0 0 1 2 2v9H2v-9a2 2 0 0 1 2-2h2zm2 2v7h8V6h-2V4zM5 15v2h3v-2zm5 0v2h3v-2zm5 0v2h3v-2z"/></svg>F. +322 619 4850</li>
    <li><svg viewBox="0 0 24 24"><path d="M2 5h20v14H2zm2 2v.5l8 5.5 8-5.5V7zm0 3v7h16v-7l-8 5.5z"/></svg>paul@pauldornevaux-example.com</li>
    <li><svg viewBox="0 0 24 24"><path d="M12 2a10 10 0 1 0 0 20 10 10 0 0 0 0-20zm-1 2.1V8H7.6A8 8 0 0 1 11 4.1zm2 0A8 8 0 0 1 16.4 8H13zM4.6 10H9v4H4.6a8 8 0 0 1 0-4zm6.4 0h2v4h-2zm4 0h4.4a8 8 0 0 1 0 4H15zM7.6 16H11v3.9A8 8 0 0 1 7.6 16zm5.4 0h3.4a8 8 0 0 1-3.4 3.9z"/></svg>www.pauldornevaux-example.com</li>
  </ul>

  <div class="studio">
    <span class="studio-mark"></span>
    <span class="studio-name">Paul Dornevaux Studio</span>
  </div>

  <address class="address">
    14 rue des Marronniers<br>1420 Waterloo<br>Belgium
  </address>
</article>
</body>
</html>
```